Design mobile friendly review and ranking site

We're working on a corporate website for reviewing and ranking fellow employees. We need the website to look both fun and professional and it needs to be responsive - to it works on mobile and desktop.

Looking for css and HTML for 3 key pages as well as a header and footer for the site. Also would need any supporting graphics as part of the design.

Target Market(s)

Professionals in their 20s, 30s, and 40s.

Industry/Entity Type

Internet

Coding

Coded - Design and coding required

Number of Pages Required

3 page

Font styles to use
Sans Serif

Requirements
Must have
• 3 key pages we need (note included screenshots for each - these are just super rough cuts so you see examples of the content.)
• a) main-intro: A compelling into page with a login/registration form. Should be sleek/modern/enticing. Also we would show the ranking for the top 3 people to tease people re: content.
• b) main-page: Has two sections: One at the top where you would rate someone and one at the bottom where it shows a ranking of people.
• c) profile page: This is where you view a specific person. You see the person's picture, some info about the person, you see their overall rating, you can rate them, and you also see their historical ratings.
Nice to have
• Note we need css and HTML for this. It should feel as sleek and modern. Note also must be responsive design so it works well in mobile and desktop.

```html
<!DOCTYPE html>
<html lang="en">
<head>
<meta charset="utf-8">
<title>Deskrank — See How People Are Ranked</title>
<link href="https://fonts.googleapis.com/css2?family=Roboto:wght@300;400;500&display=swap" rel="stylesheet">
<style>
  :root {
    --ink: #1e1e1e;
    --muted: #555;
    --teal: #259cb8;
    --teal-dark: #1b7f97;
    --green: #3f9a12;
    --green-dark: #2f7a0b;
    --gold: #f2c230;
    --star-on: #f6c21a;
    --star-off: #cfcfcf;
    --page: #d5eaf2;
    --card: #ffffff;
    --cta: #2b3338;
  }
  * { box-sizing: border-box; margin: 0; padding: 0; }
  html, body { width: 1041px; height: 1200px; overflow: hidden; }
  body { font-family: "Roboto", sans-serif; color: var(--ink); background: var(--page); position: relative; }

  .site-header { position: absolute; left: 0; top: 0; width: 1041px; height: 72px; background: #fff; }
  .brand { position: absolute; left: 68px; top: 20px; display: flex; align-items: center; gap: 8px; font-size: 28px; font-weight: 400; color: var(--teal); letter-spacing: .5px; }
  .brand-dot { width: 22px; height: 22px; border-radius: 50%; background: var(--green); }
  .header-btn { position: absolute; top: 16px; width: 100px; height: 38px; color: #fff; font-size: 14.5px; display: flex; align-items: center; justify-content: center; border-bottom: 2px solid rgba(0,0,0,.2); }
  .header-btn.login { left: 754px; background: var(--teal); }
  .header-btn.register { left: 870px; background: var(--green); }

  .hero { position: absolute; left: 0; top: 72px; width: 1041px; height: 376px; text-align: center; }
  .hero-bg { position: absolute; inset: 0; background: radial-gradient(ellipse at 50% 80%, #3a3528 0%, #1c1a16 45%, #0b0a08 100%); }
  .hero-title { position: absolute; left: 0; right: 0; top: 80px; font-weight: 300; font-size: 48px; line-height: 52px; color: #fff; }
  .hero-title .accent { color: var(--gold); font-weight: 500; }
  .hero-switch { position: absolute; left: 0; right: 0; top: 198px; font-size: 27px; font-weight: 300; }
  .hero-switch .l { color: var(--teal); }
  .hero-switch .or { color: #ddd; font-style: italic; font-size: 22px; margin: 0 6px; }
  .hero-switch .r { color: var(--green); }
  .signup { position: absolute; left: 313px; top: 266px; display: flex; gap: 13px; }
  .signup-input { width: 302px; height: 47px; background: #fff; color: #999; font-size: 19px; font-weight: 300; padding-left: 16px; display: flex; align-items: center; }
  .signup-btn { width: 100px; height: 47px; background: var(--green); color: #fff; font-size: 14.5px; font-weight: 500; display: flex; align-items: center; justify-content: center; border-bottom: 2px solid var(--green-dark); }

  .filter-bar { position: absolute; left: 0; top: 448px; width: 1041px; height: 50px; background: var(--teal); }
  .filter-select { position: absolute; left: 424px; top: 7px; width: 129px; height: 35px; background: #fff; font-size: 15px; padding-left: 18px; display: flex; align-items: center; color: #333; }
  .filter-select svg { position: absolute; right: 13px; top: 14px; }
  .filter-label { position: absolute; left: 562px; top: 15px; color: #fff; font-size: 15px; font-weight: 500; }

  .rank-card { position: absolute; left: 69px; width: 901px; height: 176px; background: var(--card); box-shadow: 0 1px 3px rgba(0,0,0,.1); }
  .avatar { position: absolute; left: 41px; top: 19px; width: 128px; height: 128px; border-radius: 50%; border: 1px solid #ddd; background: #fff; }
  .avatar-photo { position: absolute; left: 7px; top: 7px; width: 112px; height: 112px; border-radius: 50%; }
  .trophy { position: absolute; left: 182px; top: 27px; }
  .rank-label { position: absolute; left: 208px; top: 50px; font-size: 12px; color: #222; }
  .person-name { position: absolute; left: 185px; top: 63px; font-size: 23px; font-weight: 500; }
  .points { position: absolute; left: 185px; top: 103px; font-size: 15px; font-weight: 500; color: #333; }
  .reviews { position: absolute; left: 185px; top: 126px; font-size: 11.5px; color: var(--muted); }
  .reviews a { color: var(--teal-dark); text-decoration: none; font-weight: 500; }
  .ratings { position: absolute; right: 35px; top: 45px; }
  .rating-row { display: flex; align-items: center; justify-content: flex-end; height: 31.5px; gap: 15px; font-size: 13px; color: #333; }
  .stars { display: flex; gap: 5px; }

  .more-cta { position: absolute; left: 254px; top: 1100px; width: 532px; height: 52px; background: var(--cta); color: #fff; font-size: 19.5px; display: flex; align-items: center; justify-content: center; box-shadow: 0 2px 4px rgba(0,0,0,.25); }
</style>
</head>
<body>
<svg width="0" height="0" style="position:absolute">
  <defs>
    <symbol id="star" viewBox="0 0 24 24"><path d="M12 1.5l3.1 7 7.4.6-5.6 4.9 1.7 7.4L12 17.5l-6.6 3.9 1.7-7.4L1.5 9.1l7.4-.6z"/></symbol>
    <symbol id="cup" viewBox="0 0 34 36"><path d="M8 2h18v8c0 6-4 10-9 10s-9-4-9-10z M8 5H2c0 6 3 9 7 9 M26 5h6c0 6-3 9-7 9" fill="none" stroke="#c9951f" stroke-width="2"/><path d="M8 2h18v8c0 6-4 10-9 10s-9-4-9-10z" fill="#e3b13b"/><rect x="15" y="20" width="4" height="9" fill="#c9951f"/><rect x="9" y="29" width="16" height="5" fill="#7a4a12"/></symbol>
  </defs>
</svg>

<header class="site-header">
  <div class="brand"><span class="brand-dot"></span>Deskrank</div>
  <div class="header-btn login">LOGIN</div>
  <div class="header-btn register">REGISTER</div>
</header>

<section class="hero">
  <div class="hero-bg" role="img" aria-label="Dark blurred office party photo with falling gold stars"></div>
  <h1 class="hero-title">To See How People Are <span class="accent">Ranked</span><br>In Your Company</h1>
  <div class="hero-switch"><span class="l">Login</span><span class="or">or</span><span class="r">Register</span></div>
  <div class="signup">
    <div class="signup-input">Your Work Email</div>
    <div class="signup-btn">REGISTER</div>
  </div>
</section>

<div class="filter-bar">
  <div class="filter-select">Best<svg width="12" height="8" viewBox="0 0 12 8"><path d="M1 1l5 5 5-5" fill="none" stroke="#555" stroke-width="1.6"/></svg></div>
  <div class="filter-label">People</div>
</div>

<article class="rank-card" style="top:522px">
  <div class="avatar"><div class="avatar-photo" role="img" aria-label="Portrait photo of Ray Calder" style="background:linear-gradient(160deg,#b5b0a6,#6d6a66 60%,#1f2430)"></div></div>
  <svg class="trophy" width="32" height="34"><use href="#cup"/></svg>
  <div class="rank-label"># 1 Best</div>
  <h2 class="person-name">Ray Calder</h2>
  <div class="points">Point: 15</div>
  <div class="reviews">Number Of Reviews: <a href="#">1 View Details</a></div>
  <div class="ratings">
    <div class="rating-row">Smarts<span class="stars"><svg width="23" height="23" fill="var(--star-on)"><use href="#star"/></svg><svg width="23" height="23" fill="var(--star-on)"><use href="#star"/></svg><svg width="23" height="23" fill="var(--star-on)"><use href="#star"/></svg><svg width="23" height="23" fill="var(--star-off)"><use href="#star"/></svg><svg width="23" height="23" fill="var(--star-off)"><use href="#star"/></svg></span></div>
    <div class="rating-row">Easy To Work With<span class="stars"><svg width="23" height="23" fill="var(--star-on)"><use href="#star"/></svg><svg width="23" height="23" fill="var(--star-on)"><use href="#star"/></svg><svg width="23" height="23" fill="var(--star-on)"><use href="#star"/></svg><svg width="23" height="23" fill="var(--star-on)"><use href="#star"/></svg><svg width="23" height="23" fill="var(--star-on)"><use href="#star"/></svg></span></div>
    <div class="rating-row">Hard Worker<span class="stars"><svg width="23" height="23" fill="var(--star-on)"><use href="#star"/></svg><svg width="23" height="23" fill="var(--star-on)"><use href="#star"/></svg><svg width="23" height="23" fill="var(--star-on)"><use href="#star"/></svg><svg width="23" height="23" fill="var(--star-on)"><use href="#star"/></svg><svg width="23" height="23" fill="var(--star-off)"><use href="#star"/></svg></span></div>
  </div>
</article>

<article class="rank-card" style="top:706px">
  <div class="avatar"><div class="avatar-photo" role="img" aria-label="Portrait photo of Nina Marsh" style="background:linear-gradient(160deg,#c9c9c9,#8a6a55 55%,#1e2a4a)"></div></div>
  <svg class="trophy" width="32" height="34"><use href="#cup"/></svg>
  <div class="rank-label"># 2 Best</div>
  <h2 class="person-name">Nina Marsh</h2>
  <div class="points">Point: 15</div>
  <div class="reviews">Number Of Reviews: <a href="#">2 View Details</a></div>
  <div class="ratings">
    <div class="rating-row">Smarts<span class="stars"><svg width="23" height="23" fill="var(--star-on)"><use href="#star"/></svg><svg width="23" height="23" fill="var(--star-on)"><use href="#star"/></svg><svg width="23" height="23" fill="var(--star-on)"><use href="#star"/></svg><svg width="23" height="23" fill="var(--star-on)"><use href="#star"/></svg><svg width="23" height="23" fill="var(--star-on)"><use href="#star"/></svg></span></div>
    <div class="rating-row">Easy To Work With<span class="stars"><svg width="23" height="23" fill="var(--star-on)"><use href="#star"/></svg><svg width="23" height="23" fill="var(--star-on)"><use href="#star"/></svg><svg width="23" height="23" fill="var(--star-on)"><use href="#star"/></svg><svg width="23" height="23" fill="var(--star-off)"><use href="#star"/></svg><svg width="23" height="23" fill="var(--star-off)"><use href="#star"/></svg></span></div>
    <div class="rating-row">Hard Worker<span class="stars"><svg width="23" height="23" fill="var(--star-on)"><use href="#star"/></svg><svg width="23" height="23" fill="var(--star-on)"><use href="#star"/></svg><svg width="23" height="23" fill="var(--star-on)"><use href="#star"/></svg><svg width="23" height="23" fill="var(--star-on)"><use href="#star"/></svg><svg width="23" height="23" fill="var(--star-off)"><use href="#star"/></svg></span></div>
  </div>
</article>

<article class="rank-card" style="top:890px">
  <div class="avatar"><div class="avatar-photo" role="img" aria-label="Portrait photo of Owen Hale" style="background:linear-gradient(160deg,#2a2a2a,#8c6f5e 55%,#151515)"></div></div>
  <svg class="trophy" width="32" height="34"><use href="#cup"/></svg>
  <div class="rank-label"># 3 Best</div>
  <h2 class="person-name">Owen Hale</h2>
  <div class="points">Point: 15</div>
  <div class="reviews">Number Of Reviews: <a href="#">2 View Details</a></div>
  <div class="ratings">
    <div class="rating-row">Smarts<span class="stars"><svg width="23" height="23" fill="var(--star-on)"><use href="#star"/></svg><svg width="23" height="23" fill="var(--star-on)"><use href="#star"/></svg><svg width="23" height="23" fill="var(--star-on)"><use href="#star"/></svg><svg width="23" height="23" fill="var(--star-off)"><use href="#star"/></svg><svg width="23" height="23" fill="var(--star-off)"><use href="#star"/></svg></span></div>
    <div class="rating-row">Easy To Work With<span class="stars"><svg width="23" height="23" fill="var(--star-on)"><use href="#star"/></svg><svg width="23" height="23" fill="var(--star-on)"><use href="#star"/></svg><svg width="23" height="23" fill="var(--star-on)"><use href="#star"/></svg><svg width="23" height="23" fill="var(--star-on)"><use href="#star"/></svg><svg width="23" height="23" fill="var(--star-on)"><use href="#star"/></svg></span></div>
    <div class="rating-row">Hard Worker<span class="stars"><svg width="23" height="23" fill="var(--star-on)"><use href="#star"/></svg><svg width="23" height="23" fill="var(--star-on)"><use href="#star"/></svg><svg width="23" height="23" fill="var(--star-on)"><use href="#star"/></svg><svg width="23" height="23" fill="var(--star-on)"><use href="#star"/></svg><svg width="23" height="23" fill="var(--star-off)"><use href="#star"/></svg></span></div>
  </div>
</article>

<div class="more-cta">Want To See More Rankings? Log In Or Register Above</div>
</body>
</html>
```